Use Existing Logo to Design Letterhead, Envelope and Presentation Folder

We are a storm shelter company based out of Oklahoma City. We have an existing logo and brand image. We are looking for professionally designed letterhead, mailing envelopes and folders using our brand guidelines (attached). The font to be used is Futura.

The image represents simple professionalism.
We compete on quality, not price.
We value attention to detail and craftsmanship in our work.
The colors and layout are bold and clean.

Again, this is for:
1) Letterhead - contains name, address, phone, fax, and website address
2) Envelopes - logo, tagline and return address
3) Presentation Folders - logo and tag line

Our tag line is:
"America's Best EF5 Rated Storm Shelters and Family Safety Products"

Please submit your designs and once we have the initial layouts, we will provide the top designers with our contact information.

Good luck!

```html
<!DOCTYPE html>
<html lang="en">
<head>
<meta charset="utf-8">
<title>Keystone Shelters – Presentation Folder and Business Card</title>
<link rel="stylesheet" href="https://fonts.googleapis.com/css2?family=Jost:wght@400;500;600&display=swap">
<style>
  :root {
    --brand-blue: #22308f;
    --stage: #5c5c5c;
    --paper: #f1f1f1;
    --ink: #1c1c1c;
    --logo-grey: #8a8a8c;
    --storm-dark: #6e6e70;
    --storm-light: #c9c9cb;
  }
  * { box-sizing: border-box; margin: 0; padding: 0; }
  html, body { width: 1200px; height: 795px; overflow: hidden; }
  body {
    background: var(--stage);
    font-family: "Jost", "Futura", sans-serif;
    color: var(--ink);
    position: relative;
  }

  /* Folder spread */
  .folder {
    position: absolute;
    left: 40px; top: 110px;
    width: 800px; height: 560px;
    display: flex;
    gap: 4px;
  }
  .folder-panel {
    position: relative;
    width: 398px; height: 560px;
    background: var(--paper);
    overflow: hidden;
  }

  .storm-photo {
    position: absolute;
    background: linear-gradient(160deg, var(--storm-dark) 0%, #9a9a9c 45%, var(--storm-light) 75%, #8c8c8c 100%);
  }
  .rule {
    position: absolute;
    height: 5px;
    background: var(--brand-blue);
  }

  /* Back cover */
  .back-cover .storm-photo { left: 0; top: 0; width: 100%; height: 170px; }
  .back-cover .rule { left: 0; top: 170px; width: 100%; }
  .social-links {
    position: absolute;
    left: 22px; bottom: 24px;
    display: flex; gap: 6px;
  }
  .social-dot {
    width: 18px; height: 18px;
    border-radius: 50%;
    background: var(--brand-blue);
  }

  /* Front cover */
  .front-cover .brand-block {
    position: absolute;
    left: 0; top: 30px;
    width: 150px; height: 112px;
    background: var(--brand-blue);
  }
  .front-cover .intro {
    position: absolute;
    left: 168px; top: 30px;
    width: 206px;
    font-size: 10.5px;
    line-height: 1.42;
    text-align: justify;
    letter-spacing: 0.02em;
  }
  .intro strong { font-weight: 500; letter-spacing: 0.05em; }
  .front-cover .intro-mark {
    position: absolute;
    left: 168px; top: 196px;
    font-size: 11px;
    font-weight: 500;
    color: var(--brand-blue);
    letter-spacing: 0.08em;
  }
  .front-cover .rule { left: 0; top: 232px; width: 100%; }
  .front-cover .storm-photo { left: 210px; top: 237px; width: 188px; height: 210px; }

  /* Business card */
  .card {
    position: absolute;
    width: 320px; height: 186px;
    background: var(--paper);
    overflow: hidden;
  }
  .card-front { left: 860px; top: 180px; }
  .card-back { left: 860px; top: 410px; display: flex; align-items: center; justify-content: center; }

  .wordmark {
    font-weight: 500;
    color: var(--logo-grey);
    text-align: center;
    letter-spacing: 0.04em;
    line-height: 1;
  }
  .card-front .wordmark { margin-top: 26px; font-size: 24px; }
  .card-back .wordmark { font-size: 26px; }

  .contact {
    margin-top: 16px;
    text-align: center;
    font-size: 10px;
    line-height: 1.55;
    letter-spacing: 0.03em;
    color: var(--ink);
  }
  .contact .sep { padding: 0 5px; color: var(--brand-blue); }
  .card-band {
    position: absolute;
    left: 0; bottom: 0;
    width: 100%; height: 38px;
    background: var(--brand-blue);
  }
</style>
</head>
<body>

  <section class="folder" aria-label="Presentation folder">
    <article class="folder-panel back-cover">
      <div class="storm-photo" role="img" aria-label="Black and white photograph of a tornado over open plains"></div>
      <div class="rule"></div>
      <div class="social-links" aria-label="Social media">
        <span class="social-dot"></span>
        <span class="social-dot"></span>
      </div>
    </article>

    <article class="folder-panel front-cover">
      <div class="brand-block"></div>
      <p class="intro"><strong>KEYSTONE SHELTERS</strong> is an OKC-based manufacturer of the most durable, highest quality in-ground storm shelter on the market. We provide amazing customer service, the most experienced installers in the industry and back up our claims with a 10 year warranty. Whether you're in OKC, Tulsa, Kansas City, Southern Missouri, or Arkansas, we have a shelter option that can meet your unique needs.</p>
      <p class="intro-mark">KEYSTONE SHELTERS</p>
      <div class="rule"></div>
      <div class="storm-photo" role="img" aria-label="Black and white photograph of storm clouds over flat prairie"></div>
    </article>
  </section>

  <article class="card card-front" aria-label="Business card front">
    <p class="wordmark">KEYSTONE SHELTERS</p>
    <address class="contact">
      info@keystoneshelters.com<span class="sep">|</span>www.keystoneshelters.com<br>
      4820 N. Meridian Avenue, Suite 210-B<span class="sep">|</span>Oklahoma City<br>
      Phone: (405) 555-0142<span class="sep">|</span>Fax: (405) 555-0187
    </address>
    <div class="card-band"></div>
  </article>

  <article class="card card-back" aria-label="Business card back">
    <p class="wordmark">KEYSTONE SHELTERS</p>
  </article>

</body>
</html>
```